Recruitment Agency in Texas, needs a stand out header letter

Our colours are red and grey and can be found on our website
just my logo will be sufficient and address...

Target Market(s)

Engineering Manufacturing

Colors
0094D4
00A9DD
6FCCEA
C7EBF8
E9F6FB
EB3D1F
EC4F4E
F09395
F8D3D4
FCEDEE

Requirements
Must have
• use colors red and grey
Should not have
• Please use same colors and font as my logo. My website is kelbrantstaffing.com

```html
<!DOCTYPE html>
<html lang="en">
<head>
<meta charset="utf-8">
<title>KelbrantStaffing Letterhead</title>
<link href="https://fonts.googleapis.com/css2?family=Exo+2:wght@500;600&family=Open+Sans:wght@400&family=Poppins:wght@500&family=Mrs+Saint+Delafield&display=swap" rel="stylesheet">
<style>
  :root {
    --red: #e3141b;
    --grey: #5f6062;
    --ink: #3a3a3a;
    --text: #4a4a4a;
    --backdrop: #7f7c7b;
    --paper: #ffffff;
  }
  * { margin: 0; padding: 0; box-sizing: border-box; }
  html, body { width: 720px; height: 1200px; overflow: hidden; background: var(--backdrop); }
  .canvas { position: relative; width: 720px; height: 1200px; }
  .letterhead {
    position: absolute; left: 0; top: 91px;
    width: 569px; height: 804px;
    background: var(--paper);
    transform: scale(1.2654); transform-origin: 0 0;
    overflow: hidden;
  }
  .frame { position: absolute; inset: 0; width: 569px; height: 804px; }
  .brand {
    position: absolute; left: 40px; top: 40px;
    font-family: "Exo 2", sans-serif; font-weight: 600; font-size: 26px;
    color: var(--red); letter-spacing: -0.5px;
  }
  .brand-rule { position: absolute; left: 35px; top: 85px; width: 425px; height: 1px; background: var(--red); opacity: .7; }
  .subject { position: absolute; left: 40px; top: 121px; font-family: "Open Sans", sans-serif; font-size: 11px; color: var(--ink); }
  .subject-label { font-family: "Exo 2", sans-serif; font-weight: 500; font-size: 14px; margin-right: 6px; }
  .salutation { position: absolute; left: 38px; top: 186px; font-family: "Exo 2", sans-serif; font-weight: 500; font-size: 13.5px; color: var(--ink); }
  .body-copy { position: absolute; left: 38px; top: 227px; width: 499px; font-family: "Open Sans", sans-serif; font-size: 8.6px; line-height: 13px; color: var(--text); text-align: justify; }
  .body-copy p + p { margin-top: 13px; }
  .closing { position: absolute; left: 64px; top: 660px; font-family: "Exo 2", sans-serif; font-weight: 500; font-size: 14px; color: var(--ink); }
  .signature { position: absolute; left: 62px; top: 676px; font-family: "Mrs Saint Delafield", cursive; font-size: 40px; color: var(--ink); }
  .signature-rule { position: absolute; left: 64px; top: 744px; width: 83px; height: 3px; background: var(--red); }
  .contacts { position: absolute; left: 305px; top: 684px; list-style: none; font-family: "Poppins", sans-serif; font-weight: 500; font-size: 15px; color: var(--ink); }
  .contacts li { display: flex; align-items: center; height: 23.5px; }
  .contacts svg { width: 12px; height: 12px; margin-right: 7px; flex: none; }
</style>
</head>
<body>
<div class="canvas">
  <div class="letterhead">
    <svg class="frame" viewBox="0 0 569 804" aria-hidden="true">
      <rect x="0" y="0" width="569" height="12" fill="var(--red)"/>
      <rect x="0" y="0" width="12" height="804" fill="var(--red)"/>
      <polygon points="445,0 569,0 569,100" fill="var(--red)"/>
      <rect x="557" y="0" width="12" height="160" fill="var(--red)"/>
      <polygon points="569,5 483,82 569,158 569,136 510,82 569,28" fill="var(--grey)"/>
      <polygon points="536,82 569,60 569,104" fill="var(--red)"/>
      <polygon points="0,560 12,560 37,597 37,804 0,804" fill="var(--red)"/>
      <polygon points="0,640 37,625 37,634 0,649" fill="var(--paper)"/>
      <polygon points="0,690 37,675 37,684 0,699" fill="var(--paper)"/>
    </svg>

    <div class="brand">KelbrantStaffing</div>
    <div class="brand-rule"></div>

    <p class="subject"><span class="subject-label">Subjects:</span>Lorem Ipsum is simply dummy text of the printing .</p>
    <p class="salutation">Dear Mr. Jhon,</p>

    <div class="body-copy">
      <p>Lorem Ipsum is simply dummy text of the printing and typesetting industry. Lorem Ipsum has been the industry's standard dummy text ever since the 1500s, when an unknown printer took a galley of type and scrambled it to make a type specimen book. It has survived not only five centuries, but also the leap into electronic typesetting, remaining essentially unchanged. It was popularised in the 1960s with the release of Letraset sheets containing Lorem Ipsum passages, and more recently with desktop publishing software like Aldus PageMaker including versions of Lorem Ipsum.</p>
      <p>There are many variations of passages of Lorem Ipsum available, but the majority have suffered alteration in some form, by injected humour, or randomised words which don't look even slightly believable. If you are going to use a passage of Lorem Ipsum, you need to be sure there isn't anything embarrassing hidden in the middle of text. All the Lorem Ipsum generators on the Internet tend to repeat predefined chunks as necessary, making this the first true generator on the Internet. It uses a dictionary of over 200 Latin words, combined with a handful of model sentence structures, to generate Lorem Ipsum which looks reasonable. The generated Lorem Ipsum is therefore always free from repetition, injected humour, or non-characteristic words etc. The standard chunk of Lorem Ipsum used since the 1500s is reproduced below for those interested. Sections 1.10.32 and 1.10.33 from "de Finibus Bonorum et Malorum" by Cicero are also reproduced in their exact original form, accompanied by English versions from the 1914 translation by H. Rackham.</p>
      <p>It is a long established fact that a reader will be distracted by the readable content of a page when looking at its layout. The point of using Lorem Ipsum is that it has a more-or-less normal distribution of letters, as opposed to using 'Content here, content here', making it look like readable English. Many desktop publishing packages and web page editors now use Lorem Ipsum as their default model text, and a search for 'lorem ipsum' will uncover many web sites still in their infancy. Various versions have evolved over the years, sometimes by accident, sometimes on purpose (injected humour and the like).</p>
    </div>

    <p class="closing">Regards,</p>
    <p class="signature">Lorem Ipsum</p>
    <div class="signature-rule"></div>

    <ul class="contacts">
      <li><svg viewBox="0 0 12 12"><circle cx="6" cy="6" r="6" fill="var(--red)"/><path d="M4 3.2l1 1.2-.6.7a4 4 0 0 0 2.5 2.5l.7-.6 1.2 1-.6.9C6 8.7 3.3 6 3.1 3.8z" fill="#fff"/></svg>(+1)832-555-0147</li>
      <li><svg viewBox="0 0 12 12"><circle cx="6" cy="6" r="6" fill="var(--red)"/><rect x="3" y="4" width="6" height="4.2" rx=".5" fill="#fff"/><path d="M3.2 4.3L6 6.4l2.8-2.1" stroke="var(--red)" stroke-width=".7" fill="none"/></svg>info@kelbrantstaffing.com</li>
      <li><svg viewBox="0 0 12 12"><circle cx="6" cy="6" r="6" fill="var(--red)"/><circle cx="6" cy="6" r="3" fill="none" stroke="#fff" stroke-width=".8"/><path d="M3 6h6M6 3c-1.4 1.6-1.4 4.4 0 6M6 3c1.4 1.6 1.4 4.4 0 6" stroke="#fff" stroke-width=".6" fill="none"/></svg>www.kelbrantstaffing.com</li>
    </ul>
  </div>
</div>
</body>
</html>
```